Kestrim LLC, needs a web page no more than 5 pages (for now)

Kestrim is a general contractor. Our services include general contracting, design-build construction, disaster recovery and environmental remediation. Our main clients are KZE, HJ, State and Local Gov't Agencies, Hospitals and Schools. Kestrim is also a SDVOSB.

```html
<!DOCTYPE html>
<html lang="en">
<head>
<meta charset="utf-8">
<title>Kestrim LLC – General Contracting</title>
<link href="https://fonts.googleapis.com/css2?family=Poppins:wght@400;500;600;700&display=swap" rel="stylesheet">
<style>
:root{
  --gold:#c39a3c;
  --gold-dark:#a9812a;
  --ink:#1d1d1d;
  --dark:#222222;
  --footer:#1a1a1a;
  --text:#555555;
  --muted:#8a8a8a;
  --cream:#f6efe2;
  --white:#ffffff;
}
*{box-sizing:border-box;margin:0;padding:0}
html,body{width:1200px;height:4628px;overflow:hidden}
body{font-family:"Poppins",sans-serif;color:var(--ink);background:var(--white);position:relative}
.wrap{width:890px;margin:0 auto;position:relative}
.ph{display:block}
.btn{display:inline-block;background:var(--gold);color:var(--white);font-size:12px;font-weight:600;letter-spacing:.5px;text-transform:uppercase;padding:10px 22px;text-decoration:none}
.section-title{text-align:center;font-size:30px;font-weight:600;color:var(--ink)}
.arrow-link{display:inline-block;width:16px;height:10px}

/* Header */
.topbar{height:72px;display:flex;align-items:center}
.topbar .wrap{display:flex;align-items:center;justify-content:space-between}
.logo{display:flex;align-items:center;gap:8px;font-size:24px;font-weight:700;color:var(--gold);letter-spacing:1px}
.logo .dot{width:14px;height:14px;border-radius:50%;background:var(--gold)}
.top-right{display:flex;align-items:center;gap:30px}
.call{display:flex;align-items:center;gap:10px}
.call .ic{width:34px;height:34px;border-radius:50%;border:1.5px solid var(--gold);display:flex;align-items:center;justify-content:center}
.call small{display:block;font-size:10px;color:var(--muted)}
.call strong{font-size:14px;font-weight:600}
.mainnav{height:48px;background:var(--dark)}
.mainnav ul{list-style:none;display:flex;justify-content:center;height:48px;align-items:center;gap:0;padding-left:60px}
.mainnav li{font-size:13px;color:var(--white);padding:0 28px;height:48px;display:flex;align-items:center}
.mainnav li.active{background:var(--gold)}

/* Hero */
.hero{position:relative;height:580px}
.hero .ph{position:absolute;inset:0;background:linear-gradient(180deg,#5a5550 0%,#3a3632 45%,#2a2622 100%)}
.hero-content{position:absolute;top:170px;left:0;right:0;text-align:center;color:var(--white)}
.hero h1{font-size:52px;font-weight:700;line-height:1.2}
.hero p{font-size:15px;margin:14px auto 26px;width:420px;line-height:1.4}
.hero .nav-arrow{position:absolute;top:270px;width:20px;height:30px}

/* About */
.about{height:460px;position:relative}
.about .ph{position:absolute;left:0;top:0;width:560px;height:460px;background:linear-gradient(135deg,#e9edf2,#c9d3dd 60%,#b8a894)}
.about-text{position:absolute;left:620px;top:100px;width:430px}
.about-text h2{font-size:30px;font-weight:600;margin-bottom:14px}
.about-text p{font-size:13px;line-height:1.7;color:var(--text);margin-bottom:22px}

/* Services */
.services{height:880px;padding-top:60px}
.services-grid{display:grid;grid-template-columns:432px 432px;column-gap:26px;row-gap:36px;margin-top:48px}
.service .ph{height:240px}
.service h3{display:flex;justify-content:space-between;align-items:center;font-size:18px;font-weight:600;margin:16px 0 8px}
.service p{font-size:12px;color:var(--text);line-height:1.6;width:360px}

/* CTA band */
.cta{position:relative;height:300px;background:var(--gold);overflow:hidden}
.cta .ph{position:absolute;right:0;top:0;height:300px;width:720px;clip-path:polygon(12% 0,100% 0,100% 100%,0 100%)}
.cta-text{position:absolute;left:160px;top:62px;width:320px;color:var(--white)}
.cta-text h2{font-size:30px;font-weight:700;line-height:1.2}
.cta-text p{font-size:11px;line-height:1.6;margin:14px 0 18px;opacity:.95}
.btn-outline{display:inline-block;border:1px solid var(--white);color:var(--white);font-size:11px;font-weight:600;padding:8px 18px;text-transform:uppercase}

/* Clients */
.clients{height:540px;background:var(--cream);padding-top:48px}
.client-row{display:flex;justify-content:center;gap:60px;margin-top:44px}
.client{width:190px;text-align:center;font-size:13px;font-weight:500}
.seal{width:130px;height:130px;border-radius:50%;margin:0 auto 10px;display:flex;align-items:center;justify-content:center;font-size:28px;font-weight:700;color:var(--white)}
.client-row.second{margin-top:18px;gap:30px;align-items:flex-start;padding-left:40px}
.client-row.second .client{padding-top:34px}
.badge{width:110px;height:110px;border-radius:50%;background:#2f5a3a;margin:0 auto 10px}
.hospital{display:flex;align-items:flex-start;gap:12px;font-size:13px;font-weight:500}
.hospital .label{padding-top:30px}
.hospital .ph{width:240px;height:180px;background:linear-gradient(180deg,#e8eef4,#c7d2dc)}

/* Projects */
.projects{height:620px;padding-top:56px}
.project-grid{display:flex;justify-content:center;gap:28px;margin-top:56px}
.project{width:266px;text-align:center}
.project .ph{height:268px}
.project h3{font-size:15px;font-weight:500;margin:24px 0 18px}
.circle-arrow{width:40px;height:40px;border-radius:50%;border:1.5px solid var(--ink);margin:0 auto;display:flex;align-items:center;justify-content:center}
.projects .more{text-align:center;margin-top:40px}
.projects .more .btn{background:var(--dark);font-size:11px}

/* Why choose */
.why{height:440px;position:relative;padding-top:30px}
.why .ph{position:absolute;left:0;right:0;bottom:0;height:230px;background:linear-gradient(180deg,#ffffff,#ece6dc 70%,#d9cfbf)}
.why-grid{position:relative;display:flex;justify-content:center;gap:80px;margin-top:44px}
.why-item{width:220px;text-align:center}
.why-icon{width:134px;height:134px;border-radius:50%;background:var(--white);border:2px solid #e7d8b4;margin:0 auto 20px;display:flex;align-items:center;justify-content:center}
.why-item h3{font-size:15px;font-weight:600;line-height:1.4}

/* CTA 2 */
.careers{position:relative;height:340px;background:var(--gold);overflow:hidden}
.careers .ph{position:absolute;right:0;top:0;width:520px;height:340px;background:linear-gradient(135deg,#d6b36a,#a07a3a 55%,#7a6a58)}
.careers-text{position:absolute;left:160px;top:52px;width:440px;color:var(--white)}
.careers-text small{font-size:11px}
.careers-text h2{font-size:30px;font-weight:700;line-height:1.2;margin-top:4px}
.careers-text p{font-size:11px;line-height:1.6;margin:14px 0 20px;width:400px}
.btn-dark{display:inline-block;background:var(--footer);color:var(--white);font-size:11px;font-weight:600;padding:10px 24px;text-transform:uppercase;border-radius:3px}

/* Footer */
.footer{height:328px;background:var(--footer);color:#d7d7d7;position:relative}
.footer .wrap{display:flex;padding-top:40px;height:280px}
.f-brand{width:260px;padding-top:50px}
.f-brand .logo{font-size:22px}
.socials{display:flex;gap:12px;margin-top:26px}
.socials span{width:14px;height:14px;border-radius:50%;background:#d7d7d7}
.f-col h4{font-size:15px;font-weight:600;color:var(--white);margin-bottom:18px}
.f-links{width:310px}
.f-links .cols{display:flex;gap:60px}
.f-links ul{list-style:none;font-size:12px;line-height:2.4}
.f-contact ul{list-style:none;font-size:12px}
.f-contact li{display:flex;gap:10px;margin-bottom:12px;line-height:1.5}
.f-contact li svg{flex:none;margin-top:2px}
.copyright{position:absolute;bottom:0;left:0;right:0;height:48px;border-top:1px solid #333;text-align:center;font-size:11px;line-height:48px;color:#999}
</style>
</head>
<body>

<header class="topbar">
  <div class="wrap">
    <div class="logo"><span class="dot"></span>KESTRIM</div>
    <div class="top-right">
      <div class="call">
        <span class="ic"><svg width="14" height="14" viewBox="0 0 24 24"><path d="M6.6 10.8a15 15 0 0 0 6.6 6.6l2.2-2.2a1 1 0 0 1 1-.25 11.4 11.4 0 0 0 3.6.57 1 1 0 0 1 1 1V20a1 1 0 0 1-1 1A17 17 0 0 1 3 4a1 1 0 0 1 1-1h3.5a1 1 0 0 1 1 1c0 1.25.2 2.45.57 3.57a1 1 0 0 1-.25 1z" fill="#c39a3c"/></svg></span>
        <div><small>Call Us</small><strong>(555) 014-2290</strong></div>
      </div>
      <a class="btn">Start Free Quote</a>
    </div>
  </div>
</header>

<nav class="mainnav">
  <ul>
    <li class="active">Home</li><li>About</li><li>Services</li><li>Our Clients</li><li>Projects</li><li>Contact Us</li>
  </ul>
</nav>

<section class="hero">
  <div class="ph" role="img" aria-label="Construction site with excavator and workers at dusk"></div>
  <svg class="nav-arrow" style="left:20px" viewBox="0 0 20 30"><path d="M14 5 4 15l10 10" stroke="#fff" stroke-width="2.5" fill="none"/></svg>
  <svg class="nav-arrow" style="right:20px" viewBox="0 0 20 30"><path d="M6 5l10 10-10 10" stroke="#fff" stroke-width="2.5" fill="none"/></svg>
  <div class="hero-content">
    <h1>Building with Precision<br>Serving with Kestrim</h1>
    <p>General Contracting • Design Build • Disaster Recovery • Environmental Remediation</p>
    <a class="btn">Work With Us</a>
  </div>
</section>

<section class="about">
  <div class="ph" role="img" aria-label="Two engineers in hard hats reviewing building plans"></div>
  <div class="about-text">
    <h2>About Us</h2>
    <p>Lorem Ipsum is simply dummy text of the printing and typesetting industry. Lorem Ipsum has been the industry's standard dummy text ever since the 1500s, when an unknown printer took a galley of type and scrambled it to make a type specimen book.</p>
    <p>Lorem Ipsum is simply dummy text of the printing and typesetting industry. Lorem Ipsum has been the industry's standard dummy specimen book.</p>
    <a class="btn">Learn More</a>
  </div>
</section>

<section class="services">
  <h2 class="section-title">Our Services</h2>
  <div class="wrap services-grid">
    <article class="service">
      <div class="ph" role="img" aria-label="Contractors shaking hands on a job site" style="background:linear-gradient(135deg,#c9b796,#8f7a5c)"></div>
      <h3>General Contracting<svg class="arrow-link" viewBox="0 0 16 10"><path d="M0 5h14M10 1l4 4-4 4" stroke="#1d1d1d" stroke-width="1.4" fill="none"/></svg></h3>
      <p>Complete project oversight from planning to handover, so every build stays on time and on budget.</p>
    </article>
    <article class="service">
      <div class="ph" role="img" aria-label="Engineers in safety vests reviewing a tablet on site" style="background:linear-gradient(135deg,#b8c4cf,#d8a24a)"></div>
      <h3>Design-Build Construction<svg class="arrow-link" viewBox="0 0 16 10"><path d="M0 5h14M10 1l4 4-4 4" stroke="#1d1d1d" stroke-width="1.4" fill="none"/></svg></h3>
      <p>One team carries design and construction together, so your project moves faster with fewer surprises.</p>
    </article>
    <article class="service">
      <div class="ph" role="img" aria-label="Damaged building after a disaster" style="background:linear-gradient(180deg,#a9b4bd,#6e6a62)"></div>
      <h3>Disaster Recovery<svg class="arrow-link" viewBox="0 0 16 10"><path d="M0 5h14M10 1l4 4-4 4" stroke="#1d1d1d" stroke-width="1.4" fill="none"/></svg></h3>
      <p>Rapid response crews restore damaged sites and get communities safely back to work.</p>
    </article>
    <article class="service">
      <div class="ph" role="img" aria-label="Field workers testing soil in a wooded area" style="background:linear-gradient(135deg,#7d8a5a,#c7b27a)"></div>
      <h3>Environmental Remediation<svg class="arrow-link" viewBox="0 0 16 10"><path d="M0 5h14M10 1l4 4-4 4" stroke="#1d1d1d" stroke-width="1.4" fill="none"/></svg></h3>
      <p>Careful cleanup of contaminated land and structures to meet every safety standard.</p>
    </article>
  </div>
</section>

<section class="cta">
  <div class="ph" role="img" aria-label="Architect drawing plans at a desk" style="background:linear-gradient(135deg,#f1ede6,#d4cabb 60%,#b9a98f)"></div>
  <div class="cta-text">
    <h2>Ready To Start Your Next Project With Kestrim?</h2>
    <p>Our team helps agencies and owners plan, build and restore with care. Reach out today and we will map your next project together.</p>
    <span class="btn-outline">Contact Us</span>
  </div>
</section>

<section class="clients">
  <h2 class="section-title">Our Clients</h2>
  <div class="client-row">
    <div class="client"><div class="seal" style="background:#1f3a6b">KZE</div>KZE</div>
    <div class="client"><div class="seal" style="background:#23315a">HJ</div>HJ</div>
    <div class="client"><div class="seal" style="background:transparent;color:#1f3a6b;font-size:26px">Scholara</div>Schools</div>
  </div>
  <div class="client-row second">
    <div class="client"><div class="badge"></div>State and Local<br>Gov't Agencies</div>
    <div class="hospital">
      <span class="label">Hospitals</span>
      <div class="ph" role="img" aria-label="Modern hospital building"></div>
    </div>
  </div>
</section>

<section class="projects">
  <h2 class="section-title">Our Projects</h2>
  <div class="project-grid">
    <div class="project"><div class="ph" role="img" aria-label="Soldiers at a renovated military facility" style="background:linear-gradient(180deg,#5e5a4c,#2f2c26)"></div><h3>Military / KZE Renovations</h3><div class="circle-arrow"><svg width="16" height="10" viewBox="0 0 16 10"><path d="M0 5h14M10 1l4 4-4 4" stroke="#1d1d1d" stroke-width="1.4" fill="none"/></svg></div></div>
    <div class="project"><div class="ph" role="img" aria-label="Hospital building under construction with crane" style="background:linear-gradient(180deg,#c9cdd0,#8a6f55)"></div><h3>Hospital Renovations</h3><div class="circle-arrow"><svg width="16" height="10" viewBox="0 0 16 10"><path d="M0 5h14M10 1l4 4-4 4" stroke="#1d1d1d" stroke-width="1.4" fill="none"/></svg></div></div>
    <div class="project"><div class="ph" role="img" aria-label="Electricians working on wiring" style="background:linear-gradient(135deg,#d7c2a0,#c06a2e)"></div><h3>Electrical</h3><div class="circle-arrow"><svg width="16" height="10" viewBox="0 0 16 10"><path d="M0 5h14M10 1l4 4-4 4" stroke="#1d1d1d" stroke-width="1.4" fill="none"/></svg></div></div>
    <div class="project"><div class="ph" role="img" aria-label="Road paving crew at night" style="background:linear-gradient(180deg,#3c4650,#1e2226)"></div><h3>Roadway</h3><div class="circle-arrow"><svg width="16" height="10" viewBox="0 0 16 10"><path d="M0 5h14M10 1l4 4-4 4" stroke="#1d1d1d" stroke-width="1.4" fill="none"/></svg></div></div>
  </div>
  <div class="more"><a class="btn">View All Projects</a></div>
</section>

<section class="why">
  <div class="ph" role="img" aria-label="Hands reviewing blueprints on a table"></div>
  <h2 class="section-title" style="position:relative">Why Choose Kestrim</h2>
  <div class="why-grid">
    <div class="why-item">
      <div class="why-icon"><svg width="54" height="54" viewBox="0 0 54 54" fill="none" stroke="#c39a3c" stroke-width="2"><circle cx="27" cy="16" r="7"/><circle cx="12" cy="22" r="5"/><circle cx="42" cy="22" r="5"/><path d="M15 44c0-8 5-14 12-14s12 6 12 14M3 42c0-6 4-10 9-10M51 42c0-6-4-10-9-10"/></svg></div>
      <h3>Veteran-Owned Expertise (SDVOSB)</h3>
    </div>
    <div class="why-item">
      <div class="why-icon"><svg width="50" height="54" viewBox="0 0 50 54" fill="none" stroke="#c39a3c" stroke-width="2"><path d="M8 4h24l10 10v36H8z"/><path d="M32 4v10h10M15 22h20M15 30h20M15 38h12"/></svg></div>
      <h3>Government Contracting Experience</h3>
    </div>
    <div class="why-item">
      <div class="why-icon"><svg width="48" height="54" viewBox="0 0 48 54" fill="none" stroke="#c39a3c" stroke-width="2"><path d="M24 3 5 10v16c0 13 8 21 19 25 11-4 19-12 19-25V10z"/><path d="m15 27 7 7 12-13"/></svg></div>
      <h3>Precision, Safety, And Compliance</h3>
    </div>
  </div>
</section>

<section class="careers">
  <div class="ph" role="img" aria-label="Two workers in hard hats looking over a building site"></div>
  <div class="careers-text">
    <small>Careers</small>
    <h2>Ready To Start Your<br>Next Project With Kestrim?</h2>
    <p>Lorem Ipsum is simply dummy text of the printing and typesetting industry. Lorem Ipsum has been the industry's standard dummy text ever since the 1500s, when an unknown printer took a galley of type and scrambled it to make a type specimen book.</p>
    <span class="btn-dark">Contact Us Today</span>
  </div>
</section>

<footer class="footer">
  <div class="wrap">
    <div class="f-brand">
      <div class="logo"><span class="dot"></span>KESTRIM</div>
      <div class="socials"><span></span><span></span><span></span><span></span></div>
    </div>
    <div class="f-col f-links">
      <h4>Quick Links</h4>
      <div class="cols">
        <ul><li>Home</li><li>About Us</li><li>Services</li><li>Contact Us</li></ul>
        <ul><li>Clients</li><li>Projects</li><li>News</li></ul>
      </div>
    </div>
    <div class="f-col f-contact">
      <h4>Contact Us</h4>
      <ul>
        <li><svg width="12" height="12" viewBox="0 0 24 24"><path d="M6.6 10.8a15 15 0 0 0 6.6 6.6l2.2-2.2a1 1 0 0 1 1-.25 11.4 11.4 0 0 0 3.6.57 1 1 0 0 1 1 1V20a1 1 0 0 1-1 1A17 17 0 0 1 3 4a1 1 0 0 1 1-1h3.5a1 1 0 0 1 1 1c0 1.25.2 2.45.57 3.57a1 1 0 0 1-.25 1z" fill="#c39a3c"/></svg>(555) 014-2290</li>
        <li><svg width="12" height="12" viewBox="0 0 24 24"><rect x="2" y="5" width="20" height="14" fill="none" stroke="#c39a3c" stroke-width="2"/><path d="m2 6 10 7 10-7" fill="none" stroke="#c39a3c" stroke-width="2"/></svg>info@kestrim.com</li>
        <li><svg width="12" height="14" viewBox="0 0 24 28"><path d="M12 2a8 8 0 0 0-8 8c0 6 8 16 8 16s8-10 8-16a8 8 0 0 0-8-8z" fill="#c39a3c"/><circle cx="12" cy="10" r="3" fill="#1a1a1a"/></svg>48 Harlow Avenue Suite 3<br>Fairmont Ridge, WI 53990 USA</li>
      </ul>
    </div>
  </div>
  <div class="copyright">© 2025 Copyright - Kestrim</div>
</footer>

</body>
</html>
```